"BrindleApps" Website Design

We are a new web/social media development company called "BrindleApps". We need a website homepage and 1 inner page designed. We want visitors to our site to know in the first few seconds that we design and build "apps". We do not want people leaving our homepage not having at least the high level understanding that we design and build "Apps".
We currently have a landing page up at www. brindleapps .example
We specialise in building bespoke
- Torvix apps
- Lumet apps
- Plimnet Apps
- Quorvel Apps
- Wendolite Apps
- Web applications
- Vub Apps
- Social Media Marketing Solutions & Strategies
We need a website design concept that is clean, crisp, fresh and says the following about us...
We are a modern web 2.0 company (simple but striking/bold)
We are friendly, professional but dynamic and NOT boring
We are experts in developing apps
We are innovative, modern, energetic and funky
We deliver quality
We can develop to all budgets
The services we offer...
1. App Consultative Services
strategy and planning services for businesses who know they should have an "App" but dont know where to start or what type of App would achieve the best ROI in relation to their objectives.
2. Persona Driven Development leading to Solution & Requirement Design
We help the client understand their audience/target market by developing typical personas of the people who they want to use the app, these personas then drive the solution and the technical requirements. During this process we also pull together written technical specs that outlines the functionality of the app including any mandatory corporate requirements, plus screen-by-screen wireframes of their app with information about page transitions/navigation and any usability requiremens
3. App Design/User Experience Design
We develop a creative look and feel that delivers an outstanding user experience.
We develop Functional Design Specs showing the planned UI (User Interface) design, including the solution design and art direction following client sign off this is passed onto the development team to be programmed along with the apps features.
4. App Development
Turning the idea into a fully functional product with great UI and UX.
5. Maintenance
We offer a range of maintenance packages to suit all budgets, but give our clients piece of mind that there is always someone to call on when problems arise.
Our target audience is
1. anyone with an "App Idea" who needs to get from idea to production
and also
2. small and medium businesses and organisations.
PLEASE NOTE - We do not want a design churned out on an existing website template, so please dont waste your time if this is your normal design process, we will only consider bespoke design concepts that have really considered our brand and needs.
We expect to need additional pages designed which we will obviously look to offer the work to the designer who we choose in this competition.
Attached is a document containing links to websites with a mobile related theme that we like so you can get a feel for our likes and expectations, in addition we have attached our company logo for use in the design.
We dont have any photos or images to use, but are more than happy to pay for stockphotos etc. that are to be used in the final design.
We have not developed the text content or header titles yet so will need placeholder text/headers in place. Once we have the design we have the intention of working the content into the design and making it very search engine friendly, so we are happy for dummy text to be used in the design process unless you feel like making the text relevant.
Thanks for all the designs so far. General feedback relating to all designs...
Although nice, at present there isnt much "personality" in the designs and in most instances there is too much noise, could you please try and simplify the designs and reduce the amount of things for someone to look at but especially reduce the amount of text read.
3. Increase the amount of space
4. Be bolder with the use of the app brand logos
5. Maybe use more images of different well known smartphone handsets.
6. Vary the size of the typography more
7. Maybe try more vibrant colour combinations, especially with the text
Thanks and good luck
Hi there,
Just to add to the design concept ideas, ive had this image in my mind of the company logo somehow taking centre stage with all things "App" bursting out of it in a fun firework type of way (so smartphones, app brand logos, little square app icons etc.)
Not sure if this is a concept anyone want to attempt to pull something together on but trying to get away from the real "corporate" look. Apps are fun, exciting and interactive, i guess i want the website and the company to get that across about our company, but still get the message across that we are quality driven.
Thanks!
Target Market(s)
and also
Industry/Entity Type
Building
Requirements
Must have
- Clean
Crisp
Not too noisy, with space to breath and read without being overloaded by info.
4 or 5 persistant navigation links (e.g. About, Services, App Platforms, Contact Us, Blog)
The inner page needs to have a subtle contact form - this shouldnt be the focus of the page but just be a feature of it as we intend to have this as a feature on most of the inner pages. The contact form needs space to add info about project, and also a note stating that by submitting their idea we are automatically guaranteeing non disclosure.
Nice to have
- Other things the homepage and maybe the inner pages
A "Join our Plimnet Fanpage"
A "Follow us on Drosk" link
A space for our drosk/blog/news feed
Should not have
- Should not be based on an off the shelf template layout

```html
<!DOCTYPE html>
<html lang="en">
<head>
<meta charset="utf-8">
<title>BrindleApps — Home</title>
<link rel="stylesheet" href="https://fonts.googleapis.com/css2?family=Arimo:wght@400;700&family=Roboto+Condensed:wght@700&family=Open+Sans:wght@300;400&display=swap">
<style>
  :root{
    --charcoal:#3a3d42;
    --charcoal-deep:#2a2c30;
    --lime:#6acd0c;
    --green:#1bb51a;
    --nav-active:#7ed321;
    --ink:#4a4f57;
    --white:#ffffff;
    --pill:#55595f;
  }
  *{margin:0;padding:0;box-sizing:border-box}
  html,body{width:1200px;height:848px;overflow:hidden;background:var(--white)}
  body{position:relative;font-family:"Arimo",Arial,sans-serif}

  .topbar{position:absolute;left:0;top:0;width:1200px;height:106px;
    background:linear-gradient(180deg,var(--charcoal-deep),var(--charcoal))}
  .hero{position:absolute;left:0;top:106px;width:1200px;height:257px;
    background:linear-gradient(90deg,var(--lime) 0%,#4cc411 40%,var(--green) 100%)}
  .statement{position:absolute;left:0;top:363px;width:1200px;height:299px;background:var(--white)}
  .band{position:absolute;left:0;top:662px;width:1200px;height:110px;
    background:linear-gradient(90deg,var(--lime),var(--green))}
  .footer{position:absolute;left:0;top:772px;width:1200px;height:76px;
    background:linear-gradient(180deg,var(--charcoal),var(--charcoal-deep))}

  .handset{position:absolute;left:47px;top:45px;width:282px;height:615px;border-radius:44px 44px 30px 30px;
    background:linear-gradient(180deg,#1a1b1d 0%,#2b2d30 60%,#cfd1d4 85%,rgba(255,255,255,0) 100%)}

  .nav{position:absolute;top:69px;left:0;font-family:"Roboto Condensed",sans-serif;font-weight:700;
    font-size:15px;color:var(--white);text-transform:uppercase}
  .nav a{position:absolute;color:inherit;text-decoration:none;white-space:nowrap}
  .nav a.is-active{color:var(--nav-active)}
  .login{position:absolute;left:998px;top:66px;color:var(--white);font-size:16px}
  .login-field{position:absolute;left:1050px;top:67px;width:112px;height:19px;border-radius:4px;background:var(--white);border:0}

  .follow-title{position:absolute;left:362px;top:166px;font-size:31px;font-weight:700;color:var(--white);letter-spacing:-1px}
  .social{position:absolute;left:362px;top:207px;width:180px;display:grid;grid-template-columns:repeat(3,60px);row-gap:14px}
  .social a{display:flex;align-items:center;gap:4px;font-size:10px;font-weight:700;color:var(--white);text-decoration:none}
  .social a::before{content:"";width:14px;height:14px;border-radius:3px;background:rgba(255,255,255,.85);flex:none}

  .cta{position:absolute;left:338px;top:309px;width:198px;height:43px;border-radius:22px;background:var(--pill);
    display:flex;align-items:center;gap:6px;padding-left:16px;color:var(--white);
    font-family:"Roboto Condensed",sans-serif;font-weight:700;font-size:14px;letter-spacing:-.3px}

  .cloud{position:absolute;left:0;top:0;color:var(--ink)}
  .cloud span{position:absolute;white-space:nowrap;font-weight:700;letter-spacing:-1px;line-height:1}
  .cloud .light{font-family:"Open Sans",sans-serif;font-weight:300;letter-spacing:-.5px}
  .cloud .reg{font-family:"Open Sans",sans-serif;font-weight:400;letter-spacing:-.5px}
  .cloud .up{transform:rotate(-90deg);transform-origin:left top;font-size:11px;letter-spacing:0}

  .footer-brand{position:absolute;left:46px;top:801px;display:flex;align-items:center;gap:5px;color:var(--white);font-size:9px}
  .footer-brand::before{content:"";width:16px;height:16px;border-radius:50%;background:var(--lime)}
  .footer-legal{position:absolute;left:128px;top:803px;font-size:9px;color:var(--white)}
  .footer-nav{position:absolute;top:803px;left:0;font-size:9px;color:var(--white)}
  .footer-nav span{position:absolute;white-space:nowrap}
</style>
</head>
<body>
  <header class="topbar"></header>
  <section class="hero"></section>
  <section class="statement"></section>
  <div class="band"></div>
  <footer class="footer"></footer>

  <div class="handset" role="img" aria-label="Smartphone with its reflection, showing the BrindleApps app on screen"></div>

  <nav class="nav">
    <a class="is-active" style="left:530px">Home</a>
    <a style="left:600px">About</a>
    <a style="left:682px">News</a>
    <a style="left:760px">Help</a>
    <a style="left:830px">Download</a>
  </nav>
  <span class="login">Login</span>
  <input class="login-field" aria-label="Login">

  <h2 class="follow-title">FollowUs</h2>
  <div class="social">
    <a>Plimnet</a><a>Drosk</a><a>Vidlo</a>
    <a>Snapra</a><a>Markly</a><a>Tumbrel</a>
  </div>

  <a class="cta">
    <svg width="16" height="10" viewBox="0 0 16 10"><path d="M2 2l6 6 6-6" fill="none" stroke="#fff" stroke-width="3" stroke-linecap="round"/></svg>
    GET A FREE TORVIX APP
  </a>

  <div class="cloud">
    <span style="left:532px;top:406px;font-size:18px">We are</span>
    <span style="left:598px;top:399px;font-size:26px">friendly</span>
    <span style="left:545px;top:430px;font-size:18px">professional but</span>
    <span style="left:690px;top:414px;font-size:40px">dynamic</span>
    <span class="up" style="left:548px;top:478px">and</span>
    <span style="left:562px;top:450px;font-size:34px">NOT boring</span>
    <span style="left:760px;top:457px;font-size:25px;letter-spacing:-.3px">We are a modern web</span>
    <span style="left:756px;top:483px;font-size:44px">2.0</span>
    <span style="left:827px;top:486px;font-size:11px;letter-spacing:0">company (simple but striking/bold)</span>
    <span class="reg" style="left:525px;top:518px;font-size:17px">We are</span>
    <span class="reg" style="left:585px;top:505px;font-size:34px">experts</span>
    <span class="reg" style="left:633px;top:543px;font-size:16px">in developing</span>
    <span class="reg" style="left:741px;top:530px;font-size:32px">apps</span>
    <span class="light" style="left:828px;top:503px;font-size:31px">We can</span>
    <span class="reg" style="left:942px;top:503px;font-size:31px">develop</span>
    <span class="light" style="left:857px;top:537px;font-size:19px">to</span>
    <span class="reg" style="left:879px;top:533px;font-size:31px">all budgets</span>
    <span style="left:955px;top:412px;font-size:15px;letter-spacing:-.3px">We are</span>
    <span style="left:1007px;top:406px;font-size:23px;letter-spacing:-.5px">innovative,</span>
    <span style="left:955px;top:428px;font-size:21px;letter-spacing:-.5px">modern,</span>
    <span class="up" style="left:1040px;top:476px;font-size:10px">energetic</span>
    <span style="left:1070px;top:428px;font-size:21px;letter-spacing:-.5px">and</span>
    <span style="left:1050px;top:442px;font-size:42px">funky</span>
    <span class="up" style="left:1062px;top:562px;font-size:13px">we</span>
    <span style="left:1076px;top:540px;font-size:25px">deliver</span>
    <span style="left:1026px;top:562px;font-size:46px">quality</span>
  </div>

  <div class="footer-brand">BrindleApps</div>
  <div class="footer-legal">© 2010 All rights reserved &nbsp;|&nbsp; Privacy Policy</div>
  <div class="footer-nav">
    <span style="left:318px">Home</span>
    <span style="left:363px">|</span>
    <span style="left:387px">About</span>
    <span style="left:430px">|</span>
    <span style="left:453px">News</span>
    <span style="left:494px">|</span>
    <span style="left:517px">Help</span>
    <span style="left:552px">|</span>
    <span style="left:575px">Download</span>
  </div>
</body>
</html>
```